Music Portal

The designer should be able to create a Landing Page Design ( Uncoded, layout only ) for ZEFTRAK.COM including Header and Footer, based on a 960 crid System.
Updates

here are some links (below the text)as examples just for you to help. we looking for something that looks clean but with differents like you see on the supporting files. we search not for the same look how the Files are, they just examples for the info from the elements that we used on the Portal.These elements must be changed within new design. please take a look on the files and read carefully the brief.
thank you very much
ZEFTRAK Team

http://grimlanterntunes.example/index.php
http://www.pebblecrowrecords.example/default.aspx?labelID=74

These Elements in the link (below the text) must be redesignt. All Elements must be changed of course, the content must be relate to Hip Hop Content.
Take a look to the link to see what elements you must designt with an new look and feel. You can choose your own structure and color to give ZEFTRAK.COM the special Look. Please read the brief carefully and take a look to the files.
Thank you

http://www.spinvaultmix.example/marco-felding
 

Hello,
please read the brief carefully because all the designs that we received are not what i'm after.
We looking for an new Design not exactly the same as on the files,these just examples for the elements that must be used in your design.
Best Regards
ZE!

Hi,
tomorrow we will update the Supporting Files. We upload the new Logo tomorrow so you can use it for your Design. Please take a look tomorrow at the Supporting files.
Best Regards
ZEFTRAK.

Target Market(s)

ZEFTRAK.COM is an Urban Music and Hip Hop specific music portal that contains various forms of content. From music videos and downloads, to Individual radio, news and charts.

Number of Pages Required

1 page

Requirements
Must have
• The Design should contain a timeless style, also relate to current Hip
• Hop or Urban Music trends with an own font and color scheme.
Nice to have

Should not have

```html
<!DOCTYPE html>
<html lang="en">
<head>
<meta charset="utf-8">
<title>ZEFTRAK – Hip Hop &amp; Urban Music Portal</title>
<link href="https://fonts.googleapis.com/css2?family=Questrial&family=PT+Sans:wght@400;700&family=Ubuntu:wght@500;700&display=swap" rel="stylesheet">
<style>
:root{
  --maroon:#7a1642;
  --pink:#c2356f;
  --pink-hero:#cc4b84;
  --pink-text:#c2306b;
  --panel:rgba(255,255,255,.18);
  --chip:#c92f6c;
  --grey-bg:#4a4a4a;
  --white:#ffffff;
  --ink:#222222;
  --soft:#f3f3f3;
  --rule:#c2356f;
}
*{margin:0;padding:0;box-sizing:border-box}
html,body{width:1200px;height:2172px;overflow:hidden;background:var(--grey-bg)}
body{font-family:"PT Sans",sans-serif;color:var(--ink)}
.page{position:relative;width:1280px;height:2317px;transform:scale(.9375);transform-origin:0 0;overflow:hidden;
  background:radial-gradient(circle at 20% 40%,#8a8a8a,#4a4a4a 60%,#3a3a3a)}
.a{position:absolute}
.masthead{left:0;top:0;width:1280px;height:96px;background:linear-gradient(#3d0418,var(--maroon))}
.logo{left:108px;top:22px;font-family:"Questrial",sans-serif;font-size:56px;color:var(--white);letter-spacing:1px;line-height:1}
.quick-search{left:881px;top:31px;width:290px;height:26px;background:#f4f4f4;border:1px solid #ddd}
.quick-search .type{position:absolute;right:0;top:0;width:98px;height:24px;border-left:1px solid #ccc;background:#fff;font-size:11px;padding:5px 9px;color:#333}
.quick-search .type::after{content:"";position:absolute;left:50px;top:10px;border:4px solid transparent;border-top-color:var(--pink)}
.navbar{left:0;top:96px;width:1280px;height:56px;background:linear-gradient(#3c3c3c,#1f1f1f)}
.main-nav{left:109px;top:110px;display:flex;font-family:"Questrial",sans-serif;font-size:24px;color:#fff}
.main-nav span.sep{margin:0 26px;color:#ccc}
.account{left:956px;top:116px;font-size:13px;font-weight:700;color:#fff;display:flex;align-items:center;gap:14px}
.crumb{left:0;top:152px;width:1280px;height:32px;background:var(--pink);color:#fff;font-size:13px;font-weight:700}
.crumb .home{position:absolute;left:108px;top:8px}
.crumb .cart{position:absolute;left:896px;top:8px;letter-spacing:.5px}
.hero{left:0;top:184px;width:1280px;height:284px;background:linear-gradient(100deg,#b93a72,var(--pink-hero) 40%,#c53f7b)}
.hero-panel{left:107px;top:193px;width:1063px;height:263px;background:var(--panel);border-radius:4px}
.hero-divider{left:726px;top:200px;height:245px;border-left:1px dotted rgba(255,255,255,.6)}
.intro{font-size:15px;font-weight:700;color:#fff;line-height:19px}
.lbl{font-size:13px;font-weight:700;color:#fff}
.chip{width:155px;height:19px;background:var(--chip);color:#fff;font-size:13px;padding:1px 5px;display:flex;justify-content:space-between;border:1px solid rgba(255,255,255,.25)}
.chip.strong{font-weight:700}
.search-box{left:772px;top:266px;width:257px;height:35px;background:#fff;border:1px solid #999}
.search-btn{left:1031px;top:266px;width:84px;height:35px;background:linear-gradient(#444,#151515);color:#fff;font-size:15px;font-weight:700;text-align:center;line-height:35px;border-radius:3px}
.popular{left:773px;top:331px;width:300px;font-size:13px;color:#fff;line-height:14.5px}
.sheet{left:107px;top:468px;width:1063px;height:1577px;background:var(--white)}
.bar{height:45px;background:linear-gradient(#434343,#1e1e1e);color:#fff;font-family:"Ubuntu",sans-serif;font-weight:500;font-size:20px;padding:10px 48px}
.bar::after{content:"";position:absolute;left:28px;bottom:-13px;border:14px solid transparent;border-bottom:0;border-top-color:#1e1e1e}
.gap{left:723px;top:468px;width:20px;height:45px;background:var(--white)}
.tabs{left:501px;top:480px;font-size:12px;font-weight:700;color:#fff;display:flex;gap:14px}
.tabs .on{border:1px solid #fff;padding:2px 10px}
.tabs .off{padding:3px 0}
.cover{width:165px;height:148px;border:2px solid #ddd}
.cap{width:165px;text-align:center;font-size:13px;line-height:15.5px;color:#555}
.cap b{color:#333}
.more{font-size:13px;font-weight:700;color:var(--pink-text);display:flex;align-items:center;gap:6px}
.more::after{content:"";border:5px solid transparent;border-right:0;border-left:6px solid #222}
.dots{left:381px;top:998px;display:flex;gap:7px}
.dots i{width:12px;height:12px;background:#444}
.dots i:first-child{background:var(--pink)}
.tile{overflow:hidden}
.tile .name{position:absolute;left:0;bottom:0;width:100%;height:24px;background:rgba(120,120,120,.55);color:#fff;font-size:13px;font-weight:700;padding:4px 12px}
.track{left:759px;width:356px;height:100px;border-bottom:1px solid var(--rule)}
.track .thumb{position:absolute;left:0;top:0;width:82px;height:73px;border:1px solid #ccc}
.play{position:absolute;width:20px;height:20px;background:#222}
.play::after{content:"";position:absolute;left:7px;top:5px;border:5px solid transparent;border-right:0;border-left:7px solid #fff}
.track .txt{position:absolute;left:123px;top:3px;width:233px;font-size:13px;line-height:14px;color:#333}
.track .band{position:absolute;left:91px;top:61px;font-size:11px;color:#777;letter-spacing:.5px}
.price{font-size:13px;font-weight:700;color:#222}
.track .price{position:absolute;left:285px;top:54px}
.cart-ic{position:absolute;width:22px;height:22px}
.pl{left:757px;width:358px}
.pl .art{position:absolute;left:0;top:0;width:135px;height:120px;box-shadow:0 3px 5px rgba(0,0,0,.35)}
.pl h3{position:absolute;left:156px;top:5px;font-family:"Ubuntu",sans-serif;font-weight:700;font-size:19px;color:var(--pink-text)}
.pl .meta{position:absolute;left:159px;font-size:13px;color:#333}
.note{background:var(--soft);font-size:11px;line-height:13px;color:#333;padding:12px 12px}
.note h4{font-size:12px;color:var(--pink-text);margin-bottom:14px;letter-spacing:.3px}
.footer{left:0;top:2045px;width:1280px;height:235px;background:linear-gradient(var(--pink),#b52d66)}
.fcol h5{font-family:"Ubuntu",sans-serif;font-size:15px;color:#fff;margin-bottom:12px;font-weight:700}
.fcol li{list-style:none;font-size:12px;color:#fff;margin-bottom:9px;padding-left:14px;position:relative}
.fcol li::before{content:"";position:absolute;left:1px;top:3px;border:4px solid transparent;border-right:0;border-left:6px solid #fff}
.paybox{left:758px;top:2103px;width:231px;height:112px;background:#fff;border:2px solid #999}
.paybox .payname{position:absolute;left:0;width:100%;text-align:center;font-size:20px;font-weight:700;color:#333}
.fnote{left:1003px;top:2100px;font-size:12px;color:#fff;line-height:30px}
.base{left:0;top:2280px;width:1280px;height:37px;background:#262626;color:#fff;font-size:11px;font-weight:700}
.base p{position:absolute;right:114px;top:14px}
</style>
</head>
<body>
<svg width="0" height="0" style="position:absolute">
  <defs>
    <symbol id="cart" viewBox="0 0 22 22">
      <circle cx="11" cy="11" r="11" fill="#c2306b"/>
      <path d="M5 7h2l2 7h7l1.5-5H8" fill="none" stroke="#fff" stroke-width="1.6"/>
      <circle cx="10" cy="16.5" r="1.2" fill="#fff"/><circle cx="15" cy="16.5" r="1.2" fill="#fff"/>
    </symbol>
    <symbol id="cart-light" viewBox="0 0 22 22">
      <circle cx="11" cy="11" r="11" fill="#ffffff"/>
      <path d="M5 7h2l2 7h7l1.5-5H8" fill="none" stroke="#c2356f" stroke-width="1.6"/>
      <circle cx="10" cy="16.5" r="1.2" fill="#c2356f"/><circle cx="15" cy="16.5" r="1.2" fill="#c2356f"/>
    </symbol>
  </defs>
</svg>
<div class="page">

  <header>
    <div class="a masthead"></div>
    <div class="a logo">ZEFTRAK</div>
    <div class="a quick-search"><span class="type">Artist</span></div>
    <div class="a navbar"></div>
    <nav class="a main-nav"><span>Music</span><span class="sep">|</span><span>Artists</span><span class="sep">|</span><span>Labels</span><span class="sep">|</span><span>Playlists</span><span class="sep">|</span><span>Top 100</span></nav>
    <div class="a account"><span>Friendhub</span><span>|</span><span>Sign Up</span><span>|</span><span>Log in</span></div>
    <div class="a crumb"><span class="home">Home</span><span class="cart">Cart: 0 Items &nbsp;| &nbsp;$ 0.00 &nbsp;&nbsp;&nbsp;Check-out</span></div>
    <svg class="a cart-ic" style="left:1146px;top:158px;width:20px;height:20px"><use href="#cart-light"/></svg>
  </header>

  <section class="a hero"></section>
  <div class="a hero-panel"></div>
  <div class="a hero-divider"></div>
  <h1 class="a intro" style="left:155px;top:209px">ZEFTRAK provides high quality MP3 Downloads<br>from all Hip Hop &amp; Urban Music Genres.</h1>
  <div class="a lbl" style="left:155px;top:259px">Filter MP3s:</div>
  <div class="a chip strong" style="left:153px;top:281px"><span>Featured Music</span><span>&gt;</span></div>
  <div class="a chip strong" style="left:339px;top:281px"><span>New Music</span><span>&gt;</span></div>
  <div class="a chip strong" style="left:520px;top:281px"><span>Upcoming Music</span><span>&gt;</span></div>
  <div class="a lbl" style="left:155px;top:314px">Browse MP3 Genre Pages:</div>
  <div class="a chip" style="left:153px;top:339px"><span>Hip Hop</span><span>11134</span></div>
  <div class="a chip" style="left:339px;top:339px"><span>Rap</span><span>00456</span></div>
  <div class="a chip" style="left:520px;top:339px"><span>R&amp;B</span><span>2557</span></div>
  <div class="a chip" style="left:153px;top:370px"><span>Soul</span><span>22354</span></div>
  <div class="a chip" style="left:339px;top:370px"><span>Grime</span><span>11247</span></div>
  <div class="a chip" style="left:520px;top:370px"><span>Trap</span><span>254</span></div>
  <div class="a chip" style="left:153px;top:400px"><span>Funk</span><span>45543</span></div>
  <div class="a chip" style="left:339px;top:400px"><span>Dancehall</span><span>57893</span></div>
  <div class="a chip" style="left:520px;top:400px"><span>DJ Choice</span><span>1245</span></div>
  <div class="a lbl" style="left:567px;top:428px">See All Generes</div>
  <div class="a lbl" style="left:773px;top:229px;font-size:15px">Search for Artist, Music or Label:</div>
  <div class="a search-box"></div>
  <div class="a search-btn">Search</div>
  <div class="a popular"><b>Popular Searches:</b><br>Rivercraft, Tobin Rask, Marco Felding, Pim Vanderhoek, Rolf Demarest, Ramon Villaseca, Glow feat. Rennick, Kai Novell, Rory Halden, Arvel, Lodgeroom Music.</div>

  <main>
    <div class="a sheet"></div>
    <div class="a bar" style="left:107px;top:468px;width:616px">Featured Releases</div>
    <div class="a gap"></div>
    <div class="a tabs"><span class="on">Singles</span><span class="off">Compilations</span></div>
    <div class="a bar" style="left:743px;top:468px;width:427px;padding-left:33px">ZEFTRAK Top 100</div>

    <svg class="a" style="left:116px;top:716px" width="24" height="52"><path d="M24 0V52L0 26Z" fill="#333"/></svg>
    <svg class="a" style="left:688px;top:716px" width="24" height="52"><path d="M0 0V52L24 26Z" fill="#333"/></svg>

    <div class="a cover" role="img" aria-label="Album cover: denim jeans photo" style="left:155px;top:545px;background:linear-gradient(#3a3a3a,#111)"></div>
    <div class="a cover" role="img" aria-label="Album cover: two men shaking hands on a studio lot" style="left:332px;top:545px;background:linear-gradient(#b9b6ae,#8a8780)"></div>
    <div class="a cover" role="img" aria-label="Album cover: artist in black leather jacket" style="left:509px;top:545px;background:linear-gradient(90deg,#f2f2f2,#1a1a1a 60%,#eee)"></div>
    <div class="a cap" style="left:155px;top:700px"><b>Title of Album</b><br>Name of Artist<br>Date DD-MM-YY</div>
    <div class="a cap" style="left:332px;top:700px"><b>Title of Album</b><br>Name of Artist<br>Date DD-MM-YY</div>
    <div class="a cap" style="left:509px;top:700px"><b>Title of Album</b><br>Name of Artist<br>Date DD-MM-YY</div>
    <div class="a cover" role="img" aria-label="Album cover: colourful crest illustration on white" style="left:155px;top:767px;background:radial-gradient(circle at 50% 42%,#e58d6a,#f3e6e0 55%,#fafafa)"></div>
    <div class="a cover" role="img" aria-label="Album cover: two figures walking in a park" style="left:332px;top:767px;background:linear-gradient(#4b5a4c,#2b3129)"></div>
    <div class="a cover" role="img" aria-label="Album cover: yellow fruit on white" style="left:509px;top:767px;background:radial-gradient(ellipse at 60% 50%,#e8d23a,#f7f3df 45%,#fafafa)"></div>
    <div class="a cap" style="left:155px;top:924px"><b>Title of Album</b><br>Name of Artist<br>Date DD-MM-YY</div>
    <div class="a cap" style="left:332px;top:924px"><b>Title of Album</b><br>Name of Artist<br>Date DD-MM-YY</div>
    <div class="a cap" style="left:509px;top:925px"><b>Title of Album</b><br>Name of Artist<br>Date DD-MM-YY</div>
    <div class="a dots"><i></i><i></i><i></i><i></i></div>
    <div class="a more" style="left:536px;top:1042px">More Feature Releases</div>

    <div class="a bar" style="left:107px;top:1092px;width:604px">Featured Artists</div>
    <div class="a tile" role="img" aria-label="Featured artist portrait" style="left:155px;top:1178px;width:238px;height:238px;background:linear-gradient(#e8e4e0,#c49a80)"><span class="name">Name</span></div>
    <div class="a tile" role="img" aria-label="Featured artist portrait" style="left:413px;top:1178px;width:135px;height:115px;background:linear-gradient(#8a6040,#c09070)"><span class="name">Name</span></div>
    <div class="a tile" role="img" aria-label="Featured artist portrait" style="left:557px;top:1178px;width:135px;height:115px;background:linear-gradient(#d8c090,#e8d8c0)"><span class="name">Name</span></div>
    <div class="a tile" role="img" aria-label="Featured artist portrait" style="left:413px;top:1302px;width:135px;height:115px;background:linear-gradient(#bbb,#555)"><span class="name">Name</span></div>
    <div class="a tile" role="img" aria-label="Featured artist portrait" style="left:557px;top:1302px;width:135px;height:115px;background:linear-gradient(#2a2420,#8a6048)"><span class="name">Name</span></div>
    <div class="a more" style="left:551px;top:1436px">More Feature Artists</div>

    <div class="a bar" style="left:107px;top:1488px;width:604px">Featured Labels</div>
    <div class="a tile" role="img" aria-label="Label artwork: profile with headphones" style="left:155px;top:1574px;width:238px;height:238px;background:linear-gradient(120deg,#d8dde6,#8e8b70)"><span class="name">Label Name</span></div>
    <div class="a tile" role="img" aria-label="Label artwork" style="left:413px;top:1574px;width:135px;height:115px;background:linear-gradient(#111,#4a4a3a)"><span class="name">Name</span></div>
    <div class="a tile" role="img" aria-label="Label artwork" style="left:557px;top:1574px;width:135px;height:115px;background:linear-gradient(#0a1a3a,#1a7aa0)"><span class="name">Name</span></div>
    <div class="a tile" role="img" aria-label="Label artwork" style="left:413px;top:1698px;width:135px;height:115px;background:#0c0c0c"><span class="name">Name</span></div>
    <div class="a tile" role="img" aria-label="Label artwork" style="left:557px;top:1698px;width:135px;height:115px;background:linear-gradient(#151515,#2a2a2a)"><span class="name">Name</span></div>
    <div class="a more" style="left:552px;top:1834px">More Feature Labels</div>

    <div class="a track" style="top:545px"><div class="thumb" role="img" aria-label="Album cover" style="background:#f0f0f0"></div><i class="play" style="left:92px;top:0"></i><p class="txt"><b>Lorem Ipsum</b> is simply dummy text<br>of the printing.</p><span class="band">Band Name</span><span class="price">$ 2.01</span><svg class="cart-ic" style="left:333px;top:50px"><use href="#cart"/></svg></div>
    <div class="a track" style="top:645px"><div class="thumb" role="img" aria-label="Album cover" style="background:linear-gradient(#6a8ab0,#2a3a4a)"></div><i class="play" style="left:92px;top:0"></i><p class="txt"><b>Lorem Ipsum</b> is simply dummy text<br>of the printing.</p><span class="band">Band Name</span><span class="price">$ 2.01</span><svg class="cart-ic" style="left:333px;top:50px"><use href="#cart"/></svg></div>
    <div class="a track" style="top:745px"><div class="thumb" role="img" aria-label="Album cover" style="background:linear-gradient(#c8b8a0,#6a4030)"></div><i class="play" style="left:92px;top:0"></i><p class="txt"><b>Lorem Ipsum</b> is simply dummy text<br>of the printing.</p><span class="band">Band Name</span><span class="price">$ 2.01</span><svg class="cart-ic" style="left:333px;top:50px"><use href="#cart"/></svg></div>
    <div class="a track" style="top:845px"><div class="thumb" role="img" aria-label="Album cover" style="background:linear-gradient(#1a1a1a,#4a5a4a)"></div><i class="play" style="left:92px;top:0"></i><p class="txt"><b>Lorem Ipsum</b> is simply dummy text<br>of the printing.</p><span class="band">Band Name</span><span class="price">$ 2.01</span><svg class="cart-ic" style="left:333px;top:50px"><use href="#cart"/></svg></div>
    <div class="a track" style="top:945px"><div class="thumb" role="img" aria-label="Album cover" style="background:linear-gradient(#d0a060,#5a4030)"></div><i class="play" style="left:92px;top:0"></i><p class="txt"><b>Lorem Ipsum</b> is simply dummy text<br>of the printing.</p><span class="band">Band Name</span><span class="price">$ 2.01</span><svg class="cart-ic" style="left:333px;top:50px"><use href="#cart"/></svg></div>
    <div class="a track" style="top:1045px"><div class="thumb" role="img" aria-label="Album cover" style="background:linear-gradient(#111,#2a2a2a)"></div><i class="play" style="left:92px;top:0"></i><p class="txt"><b>Lorem Ipsum</b> is simply dummy text<br>of the printing.</p><span class="band">Band Name</span><span class="price">$ 2.01</span><svg class="cart-ic" style="left:333px;top:50px"><use href="#cart"/></svg></div>
    <div class="a track" style="top:1145px"><div class="thumb" role="img" aria-label="Album cover" style="background:linear-gradient(#6a5a8a,#8a6a5a)"></div><i class="play" style="left:92px;top:0"></i><p class="txt"><b>Lorem Ipsum</b> is simply dummy text<br>of the printing.</p><span class="band">Band Name</span><span class="price">$ 2.01</span><svg class="cart-ic" style="left:333px;top:50px"><use href="#cart"/></svg></div>
    <div class="a track" style="top:1244px;border-bottom:0"><div class="thumb" role="img" aria-label="Album cover" style="background:linear-gradient(#3a2a2a,#6a5a4a)"></div><i class="play" style="left:92px;top:0"></i><p class="txt"><b>Lorem Ipsum</b> is simply dummy text<br>of the printing.</p><span class="band">Band Name</span><span class="price">$ 2.01</span><svg class="cart-ic" style="left:333px;top:50px"><use href="#cart"/></svg></div>
    <div class="a more" style="left:948px;top:1341px">See all top 100 tracks</div>

    <div class="a bar" style="left:759px;top:1409px;width:411px;padding-left:18px">Latest DJ Playlist</div>
    <div class="a pl" style="top:1486px;height:152px;border-bottom:1px solid var(--rule)">
      <div class="art" role="img" aria-label="Playlist cover photo" style="background:linear-gradient(#c09050,#6a4a20)"></div>
      <h3>ZEFTRAK Top Ten</h3>
      <span class="meta" style="top:25px">Artist Name</span>
      <i class="play" style="left:159px;top:51px"></i>
      <span class="meta" style="left:191px;top:53px">14 Tracks &nbsp;| &nbsp;9 Plays</span>
      <span class="meta" style="top:102px">Hip Hop</span>
      <span class="price" style="position:absolute;left:276px;top:102px">$ 22.12</span>
      <svg class="cart-ic" style="left:333px;top:97px"><use href="#cart"/></svg>
    </div>
    <div class="a pl" style="top:1666px;height:130px">
      <div class="art" role="img" aria-label="Playlist cover photo" style="background:linear-gradient(#e8e0d8,#6a5040)"></div>
      <h3>ZEFTRAK Chart</h3>
      <span class="meta" style="top:25px">Artist Name</span>
      <i class="play" style="left:159px;top:51px"></i>
      <span class="meta" style="left:191px;top:53px">12 Tracks &nbsp;| &nbsp;10 Plays</span>
      <span class="meta" style="top:102px">R&amp;B</span>
      <span class="price" style="position:absolute;left:276px;top:102px">$ 27.18</span>
      <svg class="cart-ic" style="left:333px;top:97px"><use href="#cart"/></svg>
    </div>

    <div class="a" style="left:731px;top:1870px;height:160px;border-left:1px dotted #bbb"></div>
    <div class="a note" style="left:154px;top:1886px;width:538px;height:121px"><h4>ZEFTRAK is a lead provider in legal downloads of hip hop and urban music.</h4>Download from over 800,000 high quality MP3s of Hip Hop, Rap, R&amp;B, Soul, Grime, Trap and Dancehall tracks – 320 or 128 MP3 file formats, all DRM-free. Listen and purchase releases from top DJs, artists and labels. Preview, Select, and Buy your music now on ZEFTRAK.</div>
    <div class="a note" style="left:759px;top:1886px;width:355px;height:121px"><h4>Do you have a website? Social network profile?</h4>Join our SPINVAULT Affiliate program and make easy money! Simply link to us using our unique advertising media, and get paid!<p style="text-align:center;font-size:15px;color:var(--pink-text);margin-top:14px">Join now - its free!</p></div>
  </main>

  <footer>
    <div class="a footer"></div>
    <div class="a fcol" style="left:156px;top:2080px"><h5>About Company</h5><ul><li>Imprint</li><li>About Us</li><li>Team</li><li>Jobs</li><li>Partners &amp; Friends</li></ul></div>
    <div class="a fcol" style="left:325px;top:2080px"><h5>Information</h5><ul><li>FAQ/Help</li><li>Terms &amp; Conditions</li><li>Privacy Policy</li></ul></div>
    <div class="a fcol" style="left:500px;top:2080px"><h5>More</h5><ul><li>ZEFTRAK on Friendhub</li><li>ZEFTRAK on Chirpline</li><li>ZEFTRAK Blog</li></ul></div>
    <div class="a fcol" style="left:758px;top:2080px"><h5>Payment &amp; Security</h5></div>
    <div class="a paybox">
      <span class="payname" style="top:22px">paycircuit</span>
      <span class="payname" style="top:64px">Paywell</span>
    </div>
    <div class="a fnote">TuneDeck compatible<br>Playable with all MP3 Players<br>*All prices include tax</div>
    <div class="a base"><p>Home &nbsp;| &nbsp;About Company &nbsp;| &nbsp;Contact Us &nbsp;| &nbsp;Our Links</p></div>
  </footer>

</div>
</body>
</html>
```